IT CEO and Real Estate Investor

It should include two roles and be a two sided card (both roles can be one a single side with a creative view or on different sides).
Card must be creative and interesting, but still professional.
Phone countries(USA/Russia) might be as flags or words, whatever works better.
Boris Melnovetz
Skype: boris_m
E-mail: melnovetz@quorbamail.com
Facebook: plavbook.example/melnovetz
Linkedin: trelnet.example/in/melnovetz
Phone (US): 1(555)316-2947
Phone (RUS): 7(955)482-3170
First role:
Pex Lattor (pexlattor.example) - include logo or part of logo (the $)
E-Commerce Automation Solutions
Founder/CEO/CTO
Second role:
Real Estate Investor
Cleveland, OH
UPDATE:
Let's do one side as logo only and all information on the other side - I don't like designs with information on both sides.
I also really liked designs on black (or other dark) background

```html
<!DOCTYPE html>
<html lang="en">
<head>
<meta charset="utf-8">
<title>Pex Lattor – Business Card</title>
<link rel="stylesheet" href="https://fonts.googleapis.com/css2?family=Source+Sans+3:wght@400;600&family=Montserrat:wght@500&display=swap">
<style>
  :root {
    --page: #e8e5e1;
    --card-dark: #000000;
    --brand-blue: #00aeef;
    --title-blue: #1aa3e0;
    --text-light: #e6e6e6;
    --text-muted: #bdbdbd;
    --divider: #4a4a4a;
    --swoosh-light: #ffffff;
    --swoosh-grey: #b9b9b9;
  }
  * { margin: 0; padding: 0; box-sizing: border-box; }
  html, body {
    width: 1200px; height: 987px; overflow: hidden;
    background: var(--page);
  }
  .canvas { position: relative; width: 1200px; height: 987px; }

  .card {
    position: absolute; left: 293px; width: 615px; height: 352px;
    overflow: hidden; box-shadow: 0 3px 10px rgba(0,0,0,.25);
  }
  .card--front { top: 130px; background: var(--card-dark); }
  .card--back  { top: 506px; background: var(--brand-blue); }

  .front-band { position: absolute; left: 0; top: 0; width: 615px; height: 352px; }

  .brand {
    position: absolute; left: 62px; top: 138px;
    display: flex; align-items: center; gap: 14px;
  }
  .brand__mark { width: 34px; height: 34px; background: var(--brand-blue); }
  .brand__name {
    font-family: "Montserrat", sans-serif; font-weight: 500;
    font-size: 25px; letter-spacing: 2px; color: var(--brand-blue);
  }

  .divider {
    position: absolute; left: 312px; top: 40px; width: 1px; height: 232px;
    background: var(--divider);
  }

  .details {
    position: absolute; left: 339px; top: 40px;
    font-family: "Source Sans 3", sans-serif; color: var(--text-light);
  }
  .details__name {
    font-weight: 600; font-size: 22px; letter-spacing: .5px;
    color: var(--title-blue); line-height: 1; text-transform: uppercase;
  }
  .details__role { font-size: 15px; line-height: 20px; margin-top: 6px; }
  .details__role--second { margin-top: 4px; }
  .contacts { list-style: none; margin-top: 10px; }
  .contacts li {
    display: flex; align-items: center; gap: 8px;
    font-size: 15.5px; line-height: 22px;
  }
  .contacts svg { width: 14px; height: 14px; fill: var(--title-blue); flex: none; }
  .contacts .socials { gap: 12px; margin-top: 2px; }
  .socials span { display: flex; align-items: center; gap: 6px; }
  .socials i { display: inline-block; width: 12px; height: 12px; background: var(--title-blue); }

  .back-brand {
    position: absolute; left: 0; right: 0; top: 144px; text-align: center;
    font-family: "Montserrat", sans-serif; font-weight: 500;
    font-size: 52px; line-height: 64px; letter-spacing: 4px; color: #ffffff;
  }
</style>
</head>
<body>
<main class="canvas">

  <section class="card card--front" aria-label="Card front">
    <svg class="front-band" viewBox="0 0 615 352" aria-hidden="true">
      <path d="M0 288 Q300 350 615 298 L615 352 L0 352 Z" fill="var(--brand-blue)"/>
      <path d="M0 280 Q300 338 615 290 L615 298 Q300 332 0 300 Z" fill="var(--swoosh-light)"/>
      <path d="M0 296 Q300 330 615 297 L615 302 Q300 340 0 306 Z" fill="var(--swoosh-grey)"/>
      <path d="M0 304 Q300 337 615 300 L615 304 Q300 345 0 312 Z" fill="var(--card-dark)"/>
    </svg>

    <div class="brand">
      <span class="brand__mark"></span>
      <span class="brand__name">PEX LATTOR</span>
    </div>

    <div class="divider"></div>

    <div class="details">
      <h1 class="details__name">Boris Melnovetz</h1>
      <p class="details__role">E-Commerce Automation Solutions<br>Founder/CEO/CTO</p>
      <p class="details__role details__role--second">Real Estate Investor<br>Cleveland, OH</p>
      <ul class="contacts">
        <li><svg viewBox="0 0 16 16"><path d="M3.6 1.2l2.3 2.9-1.3 1.8c.9 2 2.5 3.6 4.5 4.5l1.8-1.3 2.9 2.3-1.4 2.4C7 13.4 2.6 9 1.2 2.6z"/></svg>(US): 1(555)316-2947</li>
        <li><svg viewBox="0 0 16 16"><path d="M3.6 1.2l2.3 2.9-1.3 1.8c.9 2 2.5 3.6 4.5 4.5l1.8-1.3 2.9 2.3-1.4 2.4C7 13.4 2.6 9 1.2 2.6z"/></svg>(RUS): 7(955)482-3170</li>
        <li><svg viewBox="0 0 16 16"><path d="M1 3h14v10H1z M1.5 3.5L8 9l6.5-5.5" stroke="#000" stroke-width="1"/></svg>melnovetz@quorbamail.com</li>
        <li><svg viewBox="0 0 16 16"><circle cx="8" cy="8" r="7"/><path d="M4 5c2 0 2 2 4 2s1 3 3 3M6 12c1-1 0-3 2-3" stroke="#000" stroke-width="1.2" fill="none"/></svg>www.pexlattor.example</li>
        <li class="socials">
          <span><i></i>boris_m</span>
          <span><i></i>melnovetz</span>
          <span><i></i>melnovetz</span>
        </li>
      </ul>
    </div>
  </section>

  <section class="card card--back" aria-label="Card back">
    <div class="back-brand">PEX LATTOR</div>
  </section>

</main>
</body>
</html>
```